Business card for exciting VC company

Should look simple, crisp, and modern.

Industry/Entity Type

Venture Capital

Contact Information for Business Card

Would like to see at least one design that has our blue on the back with the tagline "Transforming Traditional Industry" and white front with contact details.

Font styles to use
Sans Serif

Requirements
Must have
• Logo

Gregory Tallis
gtallis@brindlewave.vc
Managing Partner
M (628)354-xxxx

```html
<!DOCTYPE html>
<html lang="en">
<head>
<meta charset="utf-8">
<title>Brindlewave Capital – Business Card</title>
<link href="https://fonts.googleapis.com/css2?family=Lato:wght@400;700&family=Montserrat:wght@500&display=swap" rel="stylesheet">
<style>
  :root {
    --brand-blue: #4282c5;
    --ink: #111111;
    --muted: #555a60;
    --paper: #ffffff;
    --backdrop: #e8e5e1;
  }
  html, body {
    margin: 0;
    width: 1200px;
    height: 965px;
    overflow: hidden;
    background: var(--backdrop);
  }
  .canvas {
    position: relative;
    width: 1200px;
    height: 965px;
  }
  .card {
    position: absolute;
    left: 278px;
    width: 647px;
    height: 370px;
    border-radius: 24px;
    overflow: hidden;
  }
  .card-back {
    top: 97px;
    background: var(--brand-blue);
  }
  .card-front {
    top: 503px;
    background: var(--paper);
  }
  .wordmark {
    position: absolute;
    left: 0;
    right: 0;
    text-align: center;
    font-family: "Montserrat", sans-serif;
    font-weight: 500;
    color: var(--ink);
  }
  .wordmark-name {
    display: block;
    font-size: 50px;
    letter-spacing: 3px;
    line-height: 1;
  }
  .wordmark-sub {
    display: block;
    margin-top: 14px;
    font-size: 22px;
    letter-spacing: 8px;
    line-height: 1;
  }
  .card-back .wordmark { top: 120px; }
  .card-front .wordmark { top: 44px; }
  .tagline {
    position: absolute;
    top: 228px;
    left: 0;
    right: 0;
    text-align: center;
    font-family: "Lato", sans-serif;
    font-weight: 700;
    font-size: 18px;
    color: #e8eef7;
  }
  .holder-name {
    position: absolute;
    left: 33px;
    top: 204px;
    margin: 0;
    font-family: "Lato", sans-serif;
    font-weight: 700;
    font-size: 26px;
    color: var(--ink);
  }
  .holder-title {
    position: absolute;
    left: 33px;
    top: 233px;
    padding: 0 6px 0 0;
    font-family: "Lato", sans-serif;
    font-size: 18px;
    color: var(--muted);
    background: var(--paper);
    z-index: 1;
  }
  .title-rule {
    position: absolute;
    left: 0;
    right: 0;
    top: 245px;
    height: 3px;
    background: var(--brand-blue);
  }
  .title-rule::before {
    content: "";
    position: absolute;
    left: 28px;
    width: 5px;
    height: 3px;
    background: var(--paper);
  }
  .contact-list {
    position: absolute;
    left: 33px;
    top: 275px;
    margin: 0;
    padding: 0;
    list-style: none;
    font-family: "Lato", sans-serif;
    font-size: 18px;
    color: var(--muted);
  }
  .contact-list li {
    display: flex;
    align-items: center;
    height: 23.5px;
  }
  .contact-list svg {
    width: 17px;
    height: 17px;
    margin-right: 10px;
    fill: var(--brand-blue);
  }
  .base-band {
    position: absolute;
    left: 0;
    right: 0;
    bottom: 0;
    height: 7px;
    background: var(--brand-blue);
  }
</style>
</head>
<body>
<main class="canvas">
  <section class="card card-back" aria-label="Card back">
    <div class="wordmark">
      <span class="wordmark-name">BRINDLEWAVE</span>
      <span class="wordmark-sub">CAPITAL</span>
    </div>
    <p class="tagline">TRANSFORMING TRADITIONAL INDUSTRY</p>
  </section>

  <section class="card card-front" aria-label="Card front">
    <div class="wordmark">
      <span class="wordmark-name">BRINDLEWAVE</span>
      <span class="wordmark-sub">CAPITAL</span>
    </div>
    <h1 class="holder-name">GREGORY TALLIS</h1>
    <span class="holder-title">Managing Partner</span>
    <div class="title-rule"></div>
    <ul class="contact-list">
      <li>
        <svg viewBox="0 0 24 24" aria-hidden="true"><path d="M6.6 10.8c1.4 2.8 3.8 5.1 6.6 6.6l2.2-2.2c.3-.3.7-.4 1-.2 1.1.4 2.3.6 3.6.6.6 0 1 .4 1 1V20c0 .6-.4 1-1 1C10.6 21 3 13.4 3 4c0-.6.4-1 1-1h3.5c.6 0 1 .4 1 1 0 1.3.2 2.5.6 3.6.1.3 0 .7-.2 1z"/></svg>
        (628)354-xxxx
      </li>
      <li>
        <svg viewBox="0 0 24 24" aria-hidden="true"><path d="M2 5h20v14H2z M4 7v.5l8 5 8-5V7l-8 5z" fill-rule="evenodd"/></svg>
        gtallis@brindlewave.vc
      </li>
      <li>
        <svg viewBox="0 0 24 24" aria-hidden="true"><circle cx="12" cy="12" r="10"/></svg>
        www.brindlewave.vc
      </li>
    </ul>
    <div class="base-band"></div>
  </section>
</main>
</body>
</html>
```